7:40 Steady Compass- A Handbook For Shaping Your Daily Conduct Each Morning

7:40 Steady Compass
A Handbook For Shaping Your Daily Conduct Each Morning

It will be a 6 X 9 guide that is meant for people to keep with them with pages to fill out. See supporting pics for overall pillars that are discussed and form basis of the solution.

I will need a spine and back cover as well.

My blog and content: www.morvenqlisk.com

Target Market(s)

Business professionals, senior emergency services people

Industry/Entity Type

Business Management

Font styles to use
Serif

Colors

Designer to choose colors to be used in the design.

Requirements
Must have
• Clean look, easily recognizable among other books. Front cover and back and spine. My picture on the back somewhere (corner maybe?!)
Nice to have
• Easily recognizeable
• NOTE: Graphic should read Today, Was I the Leader That I Would Want? I uploaded graphic that says ..."I Would've Wanted" which is incorrect.
Should not have
• Busy cover

```html
<!DOCTYPE html>
<html lang="en">
<head>
<meta charset="utf-8">
<title>7:40 Steady Compass – Book Cover</title>
<link rel="stylesheet" href="https://fonts.googleapis.com/css2?family=Oswald:wght@500;700&family=Raleway:wght@300;400&family=Playfair+Display:wght@400;600;700&display=swap">
<style>
  :root {
    --navy: #0a0a5c;
    --navy-deep: #070747;
    --orange: #f0950c;
    --orange-dark: #b86a06;
    --cyan: #14c8e0;
    --cyan-deep: #0a86c8;
    --white: #ffffff;
    --ink: #10106a;
  }
  * { margin: 0; padding: 0; box-sizing: border-box; }
  html, body { width: 1200px; height: 865px; overflow: hidden; background: var(--navy); }
  .cover { position: relative; width: 1200px; height: 865px; background: var(--navy); color: var(--white); overflow: hidden; }
  .abs { position: absolute; }

  /* back cover */
  .back-quote { left: 60px; top: 30px; font: 700 17px/1 "Playfair Display", serif; color: var(--orange); letter-spacing: -0.3px; }
  .back-blurb { left: 60px; top: 58px; width: 450px; font: 300 13.6px/17.2px "Raleway", sans-serif; text-align: justify; color: var(--white); }
  .back-title { left: 140px; top: 288px; font: 700 56px/56px "Playfair Display", serif; letter-spacing: -2px; }
  .gradient-text { background: linear-gradient(180deg, var(--cyan) 0%, var(--cyan-deep) 100%); -webkit-background-clip: text; background-clip: text; color: transparent; }
  .back-author { left: 215px; top: 408px; font: 400 30px/1 "Playfair Display", serif; letter-spacing: -1px; }
  .author-photo { left: 56px; top: 428px; width: 148px; height: 152px; border: 2px solid var(--cyan); background: linear-gradient(160deg, #d8d8d8, #6e6e6e); }
  .bio { font: 300 12.4px/15.6px "Raleway", sans-serif; text-align: justify; }
  .bio-top { left: 215px; top: 447px; width: 298px; }
  .bio-bottom { left: 58px; top: 589px; width: 460px; }
  .code-box { left: 359px; top: 709px; width: 188px; height: 115px; background: var(--white); z-index: 2; }

  /* band */
  .band { left: 0; top: 757px; width: 1200px; height: 81px; background: linear-gradient(180deg, var(--orange-dark) 0%, var(--orange) 55%, #f6a51c 100%); }
  .site { left: 50px; top: 777px; font: 400 34px/1 "Playfair Display", serif; color: var(--ink); letter-spacing: -1px; }
  .front-author { left: 686px; top: 764px; font: 400 62px/1 "Playfair Display", serif; color: var(--ink); letter-spacing: -3px; }

  /* spine */
  .spine-text { writing-mode: vertical-rl; white-space: nowrap; }
  .spine-number { left: 572px; top: 148px; font: 700 40px/1 "Oswald", sans-serif; color: var(--orange); }
  .spine-title { left: 576px; top: 240px; font: 600 22px/20px "Playfair Display", serif; color: var(--cyan); }
  .spine-author { left: 584px; top: 450px; font: 400 32px/1 "Playfair Display", serif; color: var(--white); letter-spacing: -1px; }

  /* front */
  .front-number { left: 830px; top: 30px; font: 700 112px/1 "Oswald", sans-serif; color: var(--orange); letter-spacing: -3px; }
  .front-title { left: 655px; top: 145px; width: 530px; font: 700 100px/96px "Playfair Display", serif; letter-spacing: -4px; text-align: center; }
  .rule { height: 1.5px; background: var(--cyan-deep); }
  .rule-top { left: 700px; top: 371px; width: 435px; }
  .rule-bottom { left: 700px; top: 405px; width: 435px; }
  .subtitle { left: 640px; top: 378px; width: 550px; text-align: center; font: 500 18.5px/1 "Oswald", sans-serif; color: var(--white); text-transform: uppercase; letter-spacing: 0.2px; }
  .hero-art { left: 632px; top: 420px; width: 568px; height: 337px; background: radial-gradient(ellipse at 55% 48%, #9fd0ff 0%, #3a63e0 28%, #1a2aa8 60%, #0b0e6a 100%); }
</style>
</head>
<body>
<main class="cover">
  <!-- back cover -->
  <p class="abs back-quote">“TODAY, WAS I THE LEADER THAT I WOULD WANT?”</p>
  <p class="abs back-blurb">Lorem ipsum dolor sit amet, consectetur adipisicing elit, sed do eiusmod tempor incididunt ut labore et dolore magna aliqua. Ut enim ad minim veniam, quis nostrud exercitation ullamco laboris nisi ut aliquip ex ea commodo consequat. Duis aute irure dolor in reprehenderit in voluptate velit esse cillum dolore eu fugiat nulla pariatur. Excepteur sint occaecat cupidatat non proident, sunt in culpa qui officia deserunt mollit anim id est laborum. Sed ut perspiciatis unde omnis iste natus error sit voluptatem accusantium doloremque laudantium, totam rem aperiam, eaque ipsa quae ab illo inventore veritatis et quasi architecto beatae vitae dicta sunt explicabo. Nemo enim ipsam voluptatem quia voluptas sit aspernatur aut odit aut fugit, sed quia consequuntur magni dolores eos qui ratione voluptatem sequi nesciunt. Neque porro quisquam est, qui dolorem ipsum quia dolor sit amet, consectetur, adipisci</p>
  <h2 class="abs back-title gradient-text">STEADY<br>COMPASS</h2>
  <p class="abs back-author">MORVEN Q. LISK</p>
  <div class="abs author-photo" role="img" aria-label="Black and white portrait photo of the author"></div>
  <p class="abs bio bio-top">Through over 25 years of experience in search and rescue and public safety Morven Lisk has found his calling going into emergencies and austere environments while everyone is heading out. Through his involvement in hundreds of emergency response missions including two of Canada’s most costly natural disasters he has accumulated vast knowledge and experience in the areas of crisis leadership, human factors,</p>
  <p class="abs bio bio-bottom">team-building and high stakes decision-making in high risk environments; those environments where the cost of error and failure is high in terms of life, personal and physical suffering, the environment, economics or brand. His extensive public safety background is matched by his corporate experience when he worked for a decade in the telecommunications sector. It was during this time he experienced a prolonged labour relations work stoppage, as well as the constant change that comes with an agile company in an ever-changing industry.</p>

  <!-- spine -->
  <p class="abs spine-text spine-number">7:40</p>
  <p class="abs spine-text spine-title">STEADY<br>COMPASS</p>
  <p class="abs spine-text spine-author">MORVEN LISK</p>

  <!-- front cover -->
  <p class="abs front-number">7:40</p>
  <h1 class="abs front-title gradient-text">STEADY<br>COMPASS</h1>
  <div class="abs rule rule-top"></div>
  <p class="abs subtitle">A Handbook For Shaping Your Daily Conduct Each Morning</p>
  <div class="abs rule rule-bottom"></div>
  <div class="abs hero-art" role="img" aria-label="Illustration of a glowing leader figure standing in the centre of a circle of blue figures"></div>

  <!-- bottom band -->
  <div class="abs band"></div>
  <div class="abs code-box"></div>
  <p class="abs site">morvenqlisk.com</p>
  <p class="abs front-author">MORVEN Q. LISK</p>
</main>
</body>
</html>
```